I need a business card design for a new company that will be doing consulting work around issues of cultural competency, and diversity and inclusion. I would like the design to be crisp and clear with bold but conservative colors and incorporate shades of blue

Target Market(s)

Small businesses, schools, non-profits

Industry/Entity Type

Consulting

Font styles to use
Serif
Sans Serif

Colors
0c5ba6
6b449b
3276b5
0292cd

Requirements
Must have
• A Morrow Venture (name of company)
• Lemlem Tavish
• CEO
• lemlem@amorrowventure.com
• (215)483-2756

```html
<!DOCTYPE html>
<html lang="en">
<head>
<meta charset="utf-8">
<title>Lemlem Tavish – Business Card</title>
<link href="https://fonts.googleapis.com/css2?family=Mulish:wght@400;800&display=swap" rel="stylesheet">
<style>
  :root {
    --backdrop: #cfcfcf;
    --card-bg: #ffffff;
    --ink: #2a2a2a;
    --navy-blue: #0c5ba6;
    --steel-blue: #3276b5;
    --sky-blue: #0292cd;
    --violet: #6b449b;
  }
  * { margin: 0; padding: 0; box-sizing: border-box; }
  html, body {
    width: 1199px;
    height: 1200px;
    overflow: hidden;
    background: var(--backdrop);
    font-family: "Mulish", sans-serif;
  }
  .business-card {
    position: absolute;
    left: 236px;
    top: 386px;
    width: 747px;
    height: 448px;
    background: var(--card-bg);
    overflow: hidden;
    color: var(--ink);
  }
  .accent-artwork {
    position: absolute;
    left: 374px;
    top: 0;
    width: 373px;
    height: 448px;
    clip-path: polygon(37% 0, 100% 0, 100% 100%, 36% 100%, 0 50%);
    background: linear-gradient(120deg, var(--violet) 0%, var(--navy-blue) 35%, var(--sky-blue) 70%, var(--steel-blue) 100%);
  }
  .identity, .company, .contact {
    position: absolute;
    text-align: center;
    white-space: nowrap;
    transform: translateX(-50%);
  }
  .identity { left: 198px; top: 70px; }
  .person-name {
    font-weight: 800;
    font-size: 48px;
    line-height: 1;
    letter-spacing: 0.5px;
  }
  .person-role {
    font-weight: 400;
    font-size: 30px;
    margin-top: 14px;
    line-height: 1;
  }
  .company {
    left: 198px;
    top: 270px;
    font-size: 26px;
    font-weight: 400;
  }
  .contact {
    left: 198px;
    top: 322px;
    font-size: 21px;
    line-height: 27px;
  }
  .contact-line { display: flex; align-items: center; justify-content: center; gap: 3px; }
  .contact-icon { width: 20px; height: 20px; fill: var(--ink); }
  .contact-icon.mail { fill: none; stroke: var(--ink); stroke-width: 1.6; }
</style>
</head>
<body>
  <section class="business-card">
    <div class="accent-artwork" role="img" aria-label="Abstract folded ribbon artwork in blue and violet"></div>

    <div class="identity">
      <h1 class="person-name">Lemlem Tavish</h1>
      <p class="person-role">CEO</p>
    </div>

    <p class="company">A Morrow Venture</p>

    <div class="contact">
      <p class="contact-line">
        <svg class="contact-icon" viewBox="0 0 24 24" aria-hidden="true"><path d="M6.6 10.8a15.1 15.1 0 0 0 6.6 6.6l2.2-2.2a1 1 0 0 1 1-.25 11.4 11.4 0 0 0 3.6.57 1 1 0 0 1 1 1V20a1 1 0 0 1-1 1A17 17 0 0 1 3 4a1 1 0 0 1 1-1h3.5a1 1 0 0 1 1 1c0 1.25.2 2.45.57 3.57a1 1 0 0 1-.25 1z"/></svg>
        <span>(215)483-2756</span>
      </p>
      <p class="contact-line">
        <svg class="contact-icon mail" viewBox="0 0 24 24" aria-hidden="true"><rect x="3" y="6" width="18" height="12"/><path d="M3 6l9 7 9-7M3 18l7-6M21 18l-7-6"/></svg>
        <span>lemlem@amorrowventure.com</span>
      </p>
    </div>
  </section>
</body>
</html>
```